Chatterloop Now Hiring Post - Automotive Mechanics

1080 x 1080 design Chatterloop ad post that we are hiring. Text to include:

We are hiring mechanics to perform suspension, brake, clutch and steering repairs on heavy duty trucks, trailers, busses and motorhomes.
Hourly wages plus performance bonus
Harbor Wellness Alliance Heath Care + Dental
401K + Company Match
Weekly Pay
3:00 pm – 11:00 pm Shift – No Weekends
Stop in anytime at Oakridge Axle Works 2718 Heron Lane, Saginaw, MI 48602
or call 989-412-7730
email you resume to axleworks@axleworks.example

Target Market(s)

Automotive mechanics / Technicians

Industry/Entity Type

Automotive

Font styles to use
Sans Serif

Colors
0054AA
0677BA
7BADD7
CADEEF
E8F1F8

Requirements
Must have
• Must include the text, our logo, and picture from our service department file = oakridge-axle-works-service.jpg
Nice to have
• Something similar to the same Pintor Motors repair ad I attached
Should not have
• No images of people. The image that we provided is from our repair shop, we would like that one used.

```html
<!DOCTYPE html>
<html lang="en">
<head>
<meta charset="utf-8">
<title>Oakridge Axle Works – We're Hiring Heavy-Duty Mechanics</title>
<link rel="stylesheet" href="https://fonts.googleapis.com/css2?family=Anton&family=Oswald:wght@400;500;600;700&family=Roboto+Condensed:ital,wght@0,400;0,700;1,700;1,800&family=Montserrat:wght@800&display=swap">
<style>
  :root {
    --ink: #0f0f10;
    --paper: #f2f2f2;
    --white: #ffffff;
    --muted: #d2d2d2;
    --blue: #1456a8;
    --red: #9e1c20;
    --red-text: #a3161b;
    --navy: #0f3f86;
  }
  * { box-sizing: border-box; margin: 0; padding: 0; }
  html, body { width: 1200px; height: 1200px; overflow: hidden; background: var(--ink); }
  .poster {
    position: relative; width: 1200px; height: 1200px; overflow: hidden;
    background: radial-gradient(ellipse at 30% 40%, #222 0%, var(--ink) 70%);
    font-family: "Oswald", sans-serif; color: var(--white);
  }
  .photo { position: absolute; }
  .photo--truck {
    left: 560px; top: 0; width: 640px; height: 560px;
    background:
      linear-gradient(90deg, var(--ink) 0%, rgba(15,15,16,0) 22%),
      linear-gradient(0deg, var(--ink) 0%, rgba(15,15,16,0) 25%),
      radial-gradient(ellipse at 55% 55%, #b3262a 0%, #6e1a1c 35%, #3a3430 60%, #2a2a2a 100%);
  }
  .photo--brakes {
    left: 380px; top: 560px; width: 820px; height: 480px;
    background:
      linear-gradient(90deg, var(--ink) 0%, rgba(15,15,16,0) 30%),
      linear-gradient(180deg, var(--ink) 0%, rgba(15,15,16,0) 18%),
      radial-gradient(ellipse at 75% 55%, #6a6357 0%, #433d34 35%, #2a2724 65%, #1a1a1a 100%);
  }
  .brand {
    position: absolute; left: 52px; top: 52px;
    display: flex; align-items: center; gap: 14px;
  }
  .brand__mark { width: 34px; height: 34px; background: var(--white); }
  .brand__name {
    font-family: "Montserrat", sans-serif; font-weight: 800; font-size: 30px;
    letter-spacing: 1px; text-transform: uppercase; color: var(--white);
  }
  .headline {
    position: absolute; display: block; font-family: "Anton", sans-serif; text-transform: uppercase;
    line-height: 1; transform-origin: left bottom; white-space: nowrap;
  }
  .headline--were { left: 30px; top: 150px; font-size: 194px; color: var(--white); transform: rotate(-5deg) scaleX(1.08); }
  .headline--hiring { left: 46px; top: 316px; font-size: 190px; color: var(--blue); transform: rotate(-6deg) scaleX(1.2); }
  .role-strip {
    position: absolute; left: 58px; top: 470px; width: 590px; height: 150px;
    transform: rotate(-11deg); transform-origin: center;
  }
  .role-strip svg { position: absolute; inset: 0; }
  .role-strip__text {
    position: absolute; left: 0; right: 0; top: 34px; text-align: center;
    font-family: "Anton", sans-serif; font-size: 64px; color: var(--ink);
    letter-spacing: -1px; transform: scaleX(0.82);
  }
  .tagline {
    position: absolute; left: 330px; top: 592px; width: 880px; height: 56px;
    transform: rotate(-8deg); transform-origin: left center;
  }
  .tagline svg { position: absolute; inset: 0; }
  .tagline__text {
    position: absolute; left: 80px; top: 6px;
    font-family: "Roboto Condensed", sans-serif; font-style: italic; font-weight: 800;
    font-size: 36px; color: var(--red-text); letter-spacing: 1px;
  }
  .perks { position: absolute; left: 16px; top: 695px; display: flex; flex-direction: column; gap: 14px; list-style: none; }
  .perk {
    width: 234px; height: 88px; background: var(--blue);
    border-radius: 14px 44px 44px 14px; display: flex; align-items: center;
    justify-content: space-between; padding: 0 22px 0 28px;
  }
  .perk__label { font-weight: 700; font-size: 30px; line-height: 0.98; text-transform: uppercase; letter-spacing: 0.5px; }
  .perk__label--tight { font-size: 28px; }
  .perk__label--big { font-size: 36px; }
  .perk__label small { display: block; font-size: 16px; font-weight: 600; }
  .perk__label .perk__note { display: block; font-size: 12px; font-weight: 500; text-transform: none; letter-spacing: 0; margin-top: 3px; }
  .perk__icon { width: 46px; height: 46px; flex: none; }
  .shift {
    position: absolute; left: 272px; top: 770px; transform: rotate(-10deg);
    transform-origin: left top; font-family: "Roboto Condensed", sans-serif;
    font-weight: 700; text-transform: uppercase; line-height: 1.2;
  }
  .shift__time { font-size: 34px; padding-left: 4px; }
  .shift__days { font-size: 44px; font-style: italic; padding-left: 30px; letter-spacing: 1px; }
  .shift__note {
    padding-left: 34px; margin-top: 10px; width: 430px;
    font-size: 19px; font-weight: 400; text-transform: none; line-height: 1.3; color: var(--muted);
  }
  .shift__note strong { color: var(--white); font-weight: 700; }
  .contact-email { position: absolute; left: 0; top: 1000px; width: 662px; height: 166px; }
  .contact-email svg.brush { position: absolute; inset: 0; }
  .contact-email__icon { position: absolute; left: 56px; top: 36px; width: 90px; height: 110px; }
  .contact-email__title {
    position: absolute; left: 170px; top: 34px;
    font-weight: 700; font-size: 40px; color: var(--navy); text-transform: uppercase;
  }
  .contact-email__address {
    position: absolute; left: 166px; top: 88px;
    font-weight: 600; font-size: 34px; color: var(--navy);
  }
  .contact-phone {
    position: absolute; left: 662px; top: 1034px; width: 538px; height: 130px;
    background: var(--red); display: flex; align-items: center; gap: 18px; padding-left: 24px;
  }
  .contact-phone__label { font-weight: 700; font-size: 48px; }
  .contact-phone__icon { width: 60px; height: 60px; margin-left: 14px; }
  .contact-phone__number { font-weight: 700; font-size: 52px; letter-spacing: 0.5px; }
  .visit {
    position: absolute; left: 0; top: 1168px; width: 1200px; height: 32px;
    display: flex; align-items: center; justify-content: center;
    font-family: "Roboto Condensed", sans-serif; font-size: 18px; color: var(--muted); letter-spacing: 0.5px;
  }
  .visit strong { color: var(--white); margin-right: 8px; }
</style>
</head>
<body>
<main class="poster">
  <div class="photo photo--truck" role="img" aria-label="Red heavy-duty truck parked inside the service bay"></div>
  <div class="photo photo--brakes" role="img" aria-label="Truck axle with brake shoes and drum assembly under repair in the shop"></div>

  <div class="brand">
    <span class="brand__mark"></span>
    <span class="brand__name">Oakridge Axle Works</span>
  </div>

  <h1>
    <span class="headline headline--were">We’re</span>
    <span class="headline headline--hiring">Hiring</span>
  </h1>

  <div class="role-strip">
    <svg viewBox="0 0 590 150" preserveAspectRatio="none" aria-hidden="true">
      <path d="M30 30 L580 8 L570 40 L590 70 L575 110 L560 140 L20 150 L0 120 L18 90 L4 60 Z" fill="var(--paper)"/>
    </svg>
    <div class="role-strip__text">HEAVY-DUTY MECHANICS</div>
  </div>

  <div class="tagline">
    <svg viewBox="0 0 880 56" preserveAspectRatio="none" aria-hidden="true">
      <path d="M0 30 L60 8 L880 0 L880 8 L90 16 L880 44 L60 56 Z" fill="var(--white)"/>
    </svg>
    <div class="tagline__text">JOIN A TEAM THAT KEEPS AMERICA MOVING</div>
  </div>

  <ul class="perks">
    <li class="perk">
      <span class="perk__label">Weekly<br>Pay</span>
      <svg class="perk__icon" viewBox="0 0 48 48" fill="none" stroke="#fff" stroke-width="3" aria-hidden="true">
        <rect x="6" y="10" width="36" height="32" rx="3"/><line x1="6" y1="19" x2="42" y2="19"/>
        <line x1="15" y1="5" x2="15" y2="13"/><line x1="33" y1="5" x2="33" y2="13"/>
        <polyline points="17,28 24,34 31,28"/>
      </svg>
    </li>
    <li class="perk">
      <span class="perk__label perk__label--tight">Health<br>Dental<span class="perk__note">Harbor Wellness Alliance</span></span>
      <svg class="perk__icon" viewBox="0 0 48 48" aria-hidden="true">
        <path d="M17 4h14v13h13v14H31v13H17V31H4V17h13z" fill="#fff"/>
      </svg>
    </li>
    <li class="perk">
      <span class="perk__label perk__label--big">401K +<small>Company Match</small></span>
      <svg class="perk__icon" viewBox="0 0 48 48" fill="none" stroke="#fff" stroke-width="3" aria-hidden="true">
        <rect x="4" y="14" width="40" height="28" rx="4"/><path d="M10 14 L30 5 L34 14"/>
        <rect x="30" y="23" width="14" height="10" rx="2"/><circle cx="36" cy="28" r="2"/>
      </svg>
    </li>
  </ul>

  <div class="shift">
    <div class="shift__time">3:00 PM–11:00 PM</div>
    <div class="shift__days">No Weekends</div>
    <p class="shift__note"><strong>Hourly wages + performance bonus.</strong> Suspension, brake, clutch and steering repairs on heavy-duty trucks, trailers, buses and motorhomes.</p>
  </div>

  <div class="contact-email">
    <svg class="brush" viewBox="0 0 662 166" preserveAspectRatio="none" aria-hidden="true">
      <path d="M0 12 L300 0 L662 8 L652 60 L662 110 L650 166 L0 166 Z" fill="var(--paper)"/>
    </svg>
    <svg class="contact-email__icon" viewBox="0 0 90 110" fill="none" stroke="var(--blue)" stroke-width="5" aria-hidden="true">
      <rect x="6" y="6" width="64" height="86" rx="6"/>
      <circle cx="38" cy="30" r="11"/>
      <line x1="18" y1="54" x2="58" y2="54"/><line x1="18" y1="66" x2="58" y2="66"/><line x1="18" y1="78" x2="46" y2="78"/>
      <path d="M70 60 L84 60 L84 104 L26 104 L26 92"/>
    </svg>
    <div class="contact-email__title">Email Your Resume</div>
    <div class="contact-email__address">axleworks@axleworks.example</div>
  </div>

  <div class="contact-phone">
    <span class="contact-phone__label">CALL</span>
    <svg class="contact-phone__icon" viewBox="0 0 60 60" aria-hidden="true">
      <path d="M10 16c0 18 16 36 34 36l6-8-9-7-6 4c-6-3-11-8-14-14l4-6-7-9z" fill="#fff"/>
      <rect x="28" y="2" width="28" height="20" rx="6" fill="#fff"/>
      <path d="M34 20 L32 28 L40 21 Z" fill="#fff"/>
      <circle cx="36" cy="12" r="2" fill="var(--red)"/><circle cx="42" cy="12" r="2" fill="var(--red)"/><circle cx="48" cy="12" r="2" fill="var(--red)"/>
    </svg>
    <span class="contact-phone__number">989-412-7730</span>
  </div>

  <p class="visit"><strong>Stop in anytime:</strong> Oakridge Axle Works · 2718 Heron Lane, Saginaw, MI 48602</p>
</main>
</body>
</html>
```